HARBORLINE AUTO GLASS

Mobile Glass Shop:

1) Windshield REPAIR 2)Windshield replacment 3) Rear Windshield Replacment 4) Side Window Replacment 5) car window replacment 6) Power Window Repair.

Schedual a service within 24 hour with one of our certified technicians.

See "brightvane auto repair" web site for referance on the nature of our buisness and service. www.brightvane-example.com

```html
<!DOCTYPE html>
<html lang="en">
<head>
<meta charset="utf-8">
<title>Harborline Auto Glass</title>
<link href="https://fonts.googleapis.com/css2?family=Oswald:wght@300;500;700&family=Montserrat:wght@400;600;700&family=Open+Sans:wght@400;600&display=swap" rel="stylesheet">
<style>
:root{
  --blue:#1aa3e8;
  --orange:#ff5a14;
  --red:#ee3a22;
  --dark:#1c212d;
  --navy:#0e1626;
  --ink:#222;
  --muted:#6b6f78;
  --white:#fff;
}
*{box-sizing:border-box;margin:0;padding:0}
html,body{width:1200px;height:4827px;overflow:hidden}
body{position:relative;background:var(--white);font-family:'Open Sans',sans-serif;color:var(--ink)}
.abs{position:absolute}
/* hero */
.hero{left:0;top:0;width:1200px;height:788px;overflow:hidden}
.hero-photo{position:absolute;inset:0;background:linear-gradient(120deg,#3c4a5a 0%,#27313f 40%,#1b2230 70%,#2a3340 100%)}
.hero-photo::after{content:"";position:absolute;inset:0;background:radial-gradient(ellipse at 30% 45%,rgba(190,60,50,.35),transparent 55%)}
.brand{left:0;width:1200px;top:30px;display:flex;justify-content:center;align-items:center;gap:12px}
.brand-mark{width:34px;height:34px;border-radius:50%;background:var(--blue)}
.brand-name{font-family:'Oswald',sans-serif;font-weight:500;font-size:30px;color:var(--white);letter-spacing:1px}
.nav{left:0;width:1200px;top:116px;display:flex;justify-content:center;gap:26px;font-family:'Oswald',sans-serif;font-size:15px;color:var(--white);text-transform:uppercase}
.nav span.dd::after{content:" ▾";font-size:11px}
.h-top{right:128px;top:336px;font-family:'Oswald',sans-serif;font-weight:700;font-size:86px;color:var(--white);line-height:1}
.h-band{left:575px;top:435px;width:625px;height:67px;background:var(--blue);clip-path:polygon(40px 0,100% 0,100% 100%,0 100%)}
.h-craft{left:660px;top:432px;font-family:'Oswald',sans-serif;font-weight:300;font-size:70px;color:var(--white);line-height:1}
.h-sub{right:105px;top:527px;font-family:'Oswald',sans-serif;font-weight:300;font-size:38px;color:var(--white)}
/* search */
.search{left:0;top:788px;width:1200px;height:196px;background:var(--dark)}
.field{top:822px;height:36px;width:242px;background:#3a3f4b;color:#ddd;font-size:12px;padding:10px 16px;border-bottom:1px solid #666}
.btn-search{left:952px;top:822px;width:156px;height:36px;background:var(--red);color:var(--white);font-size:13px;text-align:center;line-height:36px}
/* cards */
.card{top:885px;width:251px;height:356px;background:var(--white);box-shadow:0 2px 10px rgba(0,0,0,.12);text-align:center;padding:4px}
.card-photo{height:170px;width:100%}
.card h3{font-family:'Montserrat',sans-serif;font-weight:600;font-size:21px;margin:26px 0 14px;letter-spacing:.5px}
.card p{font-size:11px;line-height:21px;color:var(--muted);padding:0 12px}
.card .more{position:absolute;right:14px;bottom:20px;font-size:10px;color:var(--muted);text-transform:uppercase}
/* licensed */
.lic-photo{left:86px;top:1341px;width:501px;height:309px;background:linear-gradient(135deg,#c9ced4,#8d969f 50%,#2e6a4a)}
.lic-title{left:613px;top:1344px;width:470px;font-family:'Montserrat',sans-serif;font-weight:600;font-size:25px;line-height:26px;text-transform:uppercase}
.rule{height:2px;width:34px;background:var(--red)}
.lic-text{left:613px;top:1470px;width:490px;font-size:11px;line-height:21px;color:var(--muted)}
.lic-more{left:613px;top:1598px;font-family:'Montserrat',sans-serif;font-weight:600;font-size:11px;color:#555}
/* deal */
.deal{left:86px;top:1708px;width:677px;height:268px;background:linear-gradient(90deg,#b0574d 0%,#7a5a6c 40%,#3d5e83 75%,#8aa8c4 100%)}
.deal h3{position:absolute;left:68px;top:70px;font-family:'Montserrat',sans-serif;font-weight:700;font-size:25px;color:var(--white)}
.deal p{position:absolute;left:68px;top:116px;width:230px;font-size:14px;line-height:19px;color:var(--white)}
.news{left:788px;top:1708px;width:326px;height:268px;background:linear-gradient(135deg,#ff8a1a,#ff4d0d)}
.news h3{position:absolute;left:27px;top:30px;font-family:'Montserrat',sans-serif;font-weight:700;font-size:17px;color:var(--white)}
.news .in{position:absolute;left:27px;width:271px;height:36px;background:var(--white);font-size:10px;color:#777;padding:13px 12px}
.news .send{position:absolute;left:27px;top:186px;width:96px;height:30px;background:#222;color:var(--white);font-size:12px;font-weight:600;text-align:center;line-height:30px}
/* call */
.dark-band{left:0;top:2162px;width:1200px;height:726px;background:linear-gradient(180deg,#151b27,#1f2633 55%,#0f1420)}
.call{left:86px;top:2064px;width:1028px;height:201px;background:var(--white);box-shadow:0 4px 16px rgba(0,0,0,.12)}
.call-ico{position:absolute;left:62px;top:62px;width:78px;height:78px;background:var(--red);border-radius:8px;display:flex;align-items:center;justify-content:center}
.call h3{position:absolute;left:210px;top:66px;font-size:21px;font-weight:400;color:#222}
.call p{position:absolute;left:210px;top:102px;font-size:17px;color:var(--muted)}
.call .hire{position:absolute;left:678px;top:62px;width:276px;height:74px;background:var(--blue);border-radius:6px;color:var(--white);font-size:17px;text-align:center;padding-top:16px;line-height:21px}
/* testimonials */
.t-kicker{left:0;width:1200px;top:2332px;text-align:center;font-size:11px;color:#ccc;text-transform:uppercase}
.t-title{left:0;width:1200px;top:2352px;text-align:center;font-family:'Montserrat',sans-serif;font-weight:700;font-size:31px;color:var(--white)}
.t-rule{left:583px;top:2400px;width:34px;height:2px;background:#888}
.tcard{top:2498px;width:352px;height:240px;background:#d6d9de;padding:0 26px}
.tcard .av{position:absolute;left:28px;top:-42px;width:76px;height:76px;border-radius:50%;background:linear-gradient(#e6e6e6,#9aa0a8);border:3px solid var(--white)}
.tcard h4{margin-top:92px;font-family:'Montserrat',sans-serif;font-weight:700;font-size:15px;letter-spacing:2px;color:var(--blue);text-transform:uppercase}
.tcard p{margin-top:16px;font-size:12px;line-height:21px;color:#888}
.bar{left:248px;top:2792px;width:704px;height:6px;background:var(--white);border-radius:3px;overflow:hidden}
.bar i{display:block;width:78%;height:100%;background:var(--blue)}
/* services */
.s-kicker{left:0;width:1200px;top:2964px;text-align:center;font-size:11px;color:#666;text-transform:uppercase}
.s-title{left:0;width:1200px;top:2986px;text-align:center;font-family:'Montserrat',sans-serif;font-weight:700;font-size:31px}
.s-rule{left:583px;top:3046px;width:34px;height:2px;background:var(--red)}
.s-text{left:86px;top:3113px;width:420px;font-size:11px;line-height:21px;color:var(--muted)}
.s-box{left:86px;top:3248px;width:426px;height:225px;background:linear-gradient(180deg,#ff5a14,#ff7a1a);color:var(--white);font-size:11.5px;line-height:21px;padding:52px 28px 0 26px}
.s-box::after{content:"";position:absolute;right:-26px;top:96px;border:13px solid transparent;border-left-color:#ff6a16}
.s-list{top:3510px;list-style:none;font-size:11.5px;color:var(--muted);line-height:30px}
.s-list li::before{content:"";display:inline-block;width:8px;height:8px;border:2px solid #3a6fd1;border-radius:50%;margin-right:16px}
.s-art{left:619px;top:3122px;width:487px;height:506px;background:radial-gradient(ellipse at center,#e9f0f4 0%,#d7e6ea 45%,#fff 72%)}
/* map + contact */
.map{left:0;top:3741px;width:1200px;height:437px;background:linear-gradient(120deg,#f0efe9,#e4e6df 45%,#d8e6ef 60%,#efeee8)}
.map-tog{left:10px;top:3752px;display:flex;background:var(--white);box-shadow:0 1px 3px rgba(0,0,0,.3);font-size:14px}
.map-tog span{padding:8px 14px;color:#666}
.map-tog span.on{color:#000;font-weight:600}
.footer{left:0;top:4178px;width:1200px;height:649px;background:linear-gradient(180deg,#101a2c,#0a1220)}
.form{left:613px;top:4125px;width:488px;height:450px;background:var(--white);box-shadow:0 2px 10px rgba(0,0,0,.15);padding:28px 27px}
.form h4{font-family:'Montserrat',sans-serif;font-weight:600;font-size:15px;letter-spacing:1px}
.form small{display:block;font-size:10px;color:#999;margin-top:6px;width:400px}
.fi{position:absolute;height:40px;border:1px solid #e2e2e2;font-size:11px;color:#777;padding:12px 13px}
.fi svg{position:absolute;right:12px;top:13px}
.form .send{position:absolute;left:40px;top:382px;width:96px;height:38px;background:var(--blue);color:var(--white);font-size:12px;text-align:center;line-height:38px}
.f-h{font-size:17px;color:var(--white)}
.f-text{font-size:15px;line-height:24px;color:#aab0bb}
.f-links{list-style:none;font-size:16px;line-height:36px;color:var(--white)}
.social{left:113px;top:4608px;display:flex;gap:8px}
.social i{width:10px;height:10px;border-radius:50%;background:#c6ccd6}
.copy{left:0;width:1200px;top:4781px;text-align:center;font-size:11px;color:#8a92a0}
</style>
</head>
<body>

<section class="abs hero">
  <div class="hero-photo" role="img" aria-label="Photo of a technician in red gloves fitting a windshield in a workshop"></div>
  <div class="abs brand"><span class="brand-mark"></span><span class="brand-name">HARBORLINE AUTO GLASS</span></div>
  <nav class="abs nav"><span>Home</span><span>About us</span><span>Services</span><span>Shop</span><span class="dd">Portfolio</span><span class="dd">Blog</span><span class="dd">Shortcodes</span><span>Contact</span></nav>
  <div class="abs h-top">TOP QUALITY</div>
  <div class="abs h-band"></div>
  <div class="abs h-craft">CRAFTSMANSHIP</div>
  <div class="abs h-sub">with hands on care.</div>
</section>

<section class="abs search"></section>
<div class="abs field" style="left:114px">MARQUE</div>
<div class="abs field" style="left:403px"></div>
<div class="abs field" style="left:692px">YEAR</div>
<div class="abs btn-search">SEARCH</div>

<article class="abs card" style="left:75px"><div class="card-photo" role="img" aria-label="Technician repairing a windshield" style="background:linear-gradient(135deg,#5c7390,#2d3f55)"></div><h3>REPAIR.</h3><p>Lorem ipsum dolor sit amet, consectetur adina piscing elit. Sed blandit velit a tortor effictur in vulputate.</p><span class="more">Read more →</span></article>
<article class="abs card" style="left:341px"><div class="card-photo" role="img" aria-label="Technicians replacing a windshield" style="background:linear-gradient(135deg,#3a3f4a,#9a4048)"></div><h3>REPLACMENT.</h3><p>Lorem ipsum dolor sit amet, consectetur adina piscing elit. Sed blandit velit a tortor effictur in vulputate.</p><span class="more">Read more →</span></article>
<article class="abs card" style="left:608px"><div class="card-photo" role="img" aria-label="Window tint being applied" style="background:linear-gradient(135deg,#f4c21e,#d8361c)"></div><h3>TINT.</h3><p>Lorem ipsum dolor sit amet, consectetur adina piscing elit. Sed blandit velit a tortor effictur in vulputate.</p><span class="more">Read more →</span></article>
<article class="abs card" style="left:874px"><div class="card-photo" role="img" aria-label="Happy driver in a car" style="background:linear-gradient(135deg,#e8e2d8,#8b7a66)"></div><h3>OTHER SERVICE.</h3><p>Lorem ipsum dolor sit amet, consectetur adina piscing elit. Sed blandit velit a tortor effictur in vulputate.</p><span class="more">Read more →</span></article>

<div class="abs lic-photo" role="img" aria-label="Mechanic fitting a new windshield onto a silver car"></div>
<h2 class="abs lic-title">We are licenced experts for many major worldwide car brands</h2>
<div class="abs rule" style="left:613px;top:1442px"></div>
<p class="abs lic-text">Lorem ipsum dolor sit amet, consectetur adina, piscing elit. Sed blandit velit a tortor effictur in vulputate. Quisque malesuada dictum est neco suber ra iandimul ti posuere.Lorem ipsum dolor sit amet, consectetur adina, piscing elit. Sed blandit velit a tortor effictur in vulputate. Quisque malesu suber ra iandimul ti posuere.</p>
<div class="abs lic-more">READ MORE &nbsp;→</div>

<div class="abs deal" role="img" aria-label="Smiling driver behind the wheel">
  <h3>HURLEA DEAL</h3>
  <p>contact us todays and get 15% on all our services</p>
</div>
<div class="abs news">
  <h3>GET OUR UPDATESL</h3>
  <div class="in" style="top:92px">Your Email Address</div>
  <div class="in" style="top:139px">Your Email Address</div>
  <div class="send">SEND</div>
</div>

<section class="abs dark-band" role="img" aria-label="Dark workshop photo behind client testimonials"></section>
<div class="abs call">
  <div class="call-ico"><svg width="40" height="40" viewBox="0 0 24 24" fill="#fff"><path d="M6.6 10.8a15.1 15.1 0 0 0 6.6 6.6l2.2-2.2c.3-.3.7-.4 1-.2 1.1.4 2.3.6 3.6.6.6 0 1 .4 1 1V20c0 .6-.4 1-1 1A17 17 0 0 1 3 4c0-.6.4-1 1-1h3.5c.6 0 1 .4 1 1 0 1.3.2 2.5.6 3.6.1.3 0 .7-.2 1z"/></svg></div>
  <h3>Call Us to Get a Quote +55 786 90</h3>
  <p>Lorem ipsum dolor sit amet, commune</p>
  <div class="hire">HIRE US NOW AND<br>GET 15% OFF</div>
</div>

<div class="abs t-kicker">Testimonials</div>
<h2 class="abs t-title">FROM OUR CLIENTS</h2>
<div class="abs t-rule"></div>
<article class="abs tcard" style="left:26px"><div class="av" role="img" aria-label="Client portrait"></div><h4>Mira Castellan</h4><p>Sed elit quam, iaculis sed semper sit amet sollicit udin vitae nibh. Quisque at magna akal semper euis. Fusce commodo molestie luctus.Lorem ipsum Dolor tusima olatiup.</p></article>
<article class="abs tcard" style="left:409px"><div class="av" role="img" aria-label="Client portrait"></div><h4>Dalen Okafor</h4><p>Sed elit quam, iaculis sed semper sit amet sollicit udin vitae nibh. Quisque at magna akal semper euis. Fusce commodo molestie luctus.Lorem ipsum Dolor tusima olatiup.</p></article>
<article class="abs tcard" style="left:791px"><div class="av" role="img" aria-label="Client portrait"></div><h4>Tessa Linwood</h4><p>Sed elit quam, iaculis sed semper sit amet sollicit udin vitae nibh. Quisque at magna akal semper euis. Fusce commodo molestie luctus.Lorem ipsum Dolor tusima olatiup.</p></article>
<div class="abs bar"><i></i></div>

<div class="abs s-kicker">What we do</div>
<h2 class="abs s-title">OUR SERVICES</h2>
<div class="abs s-rule"></div>
<p class="abs s-text">Lorem ipsum dolor sit amet, consectetur adina, piscing elit. Sed blandit velit a tortor effictur in vulputate. Quisque malesuada dictum est neco suber ra iandimul ti posuere.Lorem ipsum dolor sit amet, consectetur adina, piscing elit. Sed blandit velit a tortor effictur in vulputate. Quisque malesu suber ra iandimul ti posuere.</p>
<div class="abs s-box">Whether it's front windshield, rear windshield, driver window, passenger window, or quarter glass, Harborline Auto Glass Service performs Auto Glass Replacement for every type of vehicle (car, truck, van, year, make, model, etc) in your area. We feature original equipment quality glass, free mobile service, and a national lifetime warranty on workmanship.</div>
<ul class="abs s-list" style="left:96px"><li>Ut wisi enim ad minim dolore</li><li>Veniam quis laore nostrud</li><li>Exirci tation uml hedi corper</li><li>Tirtet suscript lobortis litera</li></ul>
<ul class="abs s-list" style="left:322px"><li>Ut wisi enim ad minim dolore</li><li>Veniam quis laore nostrud</li><li>Exirci tation uml hedi corper</li><li>Tirtet suscript lobortis litera</li></ul>
<div class="abs s-art" role="img" aria-label="Illustration of a white car seen from above with its glass panels exploded outward"></div>

<div class="abs map" role="img" aria-label="Styled road map of the service area with a location pin"></div>
<div class="abs map-tog"><span>Map</span><span class="on">Styled Map</span></div>

<footer class="abs footer">
  <div class="abs f-h" style="left:99px;top:164px">Our Shops</div>
  <p class="abs f-text" style="left:99px;top:204px;width:300px">The Harborline team is the leader of floor installation and repair in the country sed diam nonumy eirmod tempor invidunt ut labore and efficient strategy.</p>
  <p class="abs f-text" style="left:99px;top:342px;width:310px">Repair in the country sed diam nonumy eirmod tempor invidunt ut labore and efficient strategy.</p>
  <div class="abs f-h" style="left:442px;top:164px">Information</div>
  <ul class="abs f-links" style="left:455px;top:194px"><li>Home</li><li>Services</li><li>About us</li><li>Contact</li><li>blog</li><li>Cart</li></ul>
</footer>
<div class="abs social"><i></i><i></i><i></i><i></i></div>
<div class="abs copy">© 2022 Harborline All rights reserved.</div>

<form class="abs form">
  <h4>Get In Touch With Us</h4>
  <small>If you have any question, Please don't hesitate to send us a message</small>
  <div class="fi" style="left:40px;top:110px;width:196px">First Name<svg width="12" height="12" viewBox="0 0 12 12" fill="#2a8de0"><circle cx="6" cy="3.5" r="3"/><path d="M0 12a6 5 0 0 1 12 0z"/></svg></div>
  <div class="fi" style="left:258px;top:110px;width:196px">Last Name<svg width="12" height="12" viewBox="0 0 12 12" fill="#2a8de0"><circle cx="6" cy="3.5" r="3"/><path d="M0 12a6 5 0 0 1 12 0z"/></svg></div>
  <div class="fi" style="left:40px;top:180px;width:196px">Phone Number<svg width="12" height="12" viewBox="0 0 12 12" fill="#2a8de0"><circle cx="6" cy="3.5" r="3"/><path d="M0 12a6 5 0 0 1 12 0z"/></svg></div>
  <div class="fi" style="left:258px;top:180px;width:196px">Your Email<svg width="14" height="11" viewBox="0 0 14 11" fill="none" stroke="#2a8de0" stroke-width="1.4"><rect x="1" y="1" width="12" height="9"/><path d="M1 1l6 5 6-5"/></svg></div>
  <div class="fi" style="left:40px;top:246px;width:414px;height:110px">Your Message<svg width="14" height="11" viewBox="0 0 14 11" fill="none" stroke="#2a8de0" stroke-width="1.4"><rect x="1" y="1" width="12" height="9"/><path d="M1 1l6 5 6-5"/></svg></div>
  <div class="send">SEND</div>
</form>

</body>
</html>
```